Rug Cleaning Web Design Project

We need a web design for our cleaning company. We currently have a web page but are not happy with its design. We currently offer fine rug cleaning,upholstery cleaning, and residential and commercial carpet cleanning. We also offer water damage restoration. For our rug cleaning services we offer : Enzyme treatments for pet contamination and odor removal, application of stain protection that is designed for the fine textiles used in rug construction, application of treatments designed to prevent moth damage and pads designed to be used under rugs.Our current web site is harborlinewash.example. We are intrested in a design with similar information to the web page of Velmora Rug Cleaners INC. We would like to use the colors that are present in our logo that will be uploaded with this description. We would also like this new page to be linked to our other address fibertendpro.example. We would like the deign to be visually attractive but not "too busy".
Updates

Please include pictures of rugs, or people washing rugs if possible. We do not offer maid type cleaning services. We would not be interested in designs including pictures depicting that type service. Thanks for your hard work on this project.

Dale Hutchins

Industry/Entity Type

Residential

Requirements
Must have
• This page must be viewable on smart phones and tablets.

```html
<!DOCTYPE html>
<html lang="en">
<head>
<meta charset="utf-8">
<title>FiberTend Pro – Harborline Cleaning, LLC</title>
<link rel="stylesheet" href="https://fonts.googleapis.com/css2?family=Arimo:wght@400;700&family=Cabin:wght@400;500&family=Crimson+Text&family=Tinos:wght@700&display=swap">
<style>
:root{
  --navy:#2b4d9c;
  --navy-dark:#23448a;
  --services-bg:#284a8e;
  --testimonial-bg:#3465cb;
  --ink:#111;
  --body-text:#333;
  --muted:#8a8a8a;
  --accent-blue:#1a63ad;
  --bullet:#f07a2a;
  --rule:#d6d6d6;
}
*{box-sizing:border-box;margin:0;padding:0}
html,body{width:1200px;height:1103px;overflow:hidden;background:#fff}
.page{position:relative;width:1420px;height:1305px;transform:scale(.84507);transform-origin:0 0;
  background:linear-gradient(#7ba5cf 0,#c9dbed 80px,#fff 135px,#fff 100%);
  font-family:Arimo,Arial,sans-serif;color:var(--body-text)}
.abs{position:absolute}
.brand{left:212px;top:28px;display:flex;align-items:center;gap:14px}
.brand-mark{width:56px;height:56px;border-radius:50%;background:var(--accent-blue)}
.brand-name{font:700 38px/1 Arimo,Arial,sans-serif;color:#222;letter-spacing:-1px}
.brand-sub{font:400 14px/1 Arimo,Arial,sans-serif;color:#222;letter-spacing:3px;margin-top:6px;text-align:right}
.search{left:979px;top:58px;width:231px;height:35px;border:1px solid #c8c8c8;background:#fff;
  font-size:12px;color:#555;padding:11px 0 0 11px}
.search svg{position:absolute;right:12px;top:11px}
.nav{left:210px;top:123px;width:997px;height:62px;background:linear-gradient(#3559a8,var(--navy-dark));
  box-shadow:0 3px 4px rgba(0,0,0,.25);display:flex;align-items:center;padding-left:6px}
.nav a{font:700 15px/1 Tinos,"Times New Roman",serif;color:#fff;text-decoration:none;padding:0 18px;
  border-right:1px solid rgba(255,255,255,.18);height:26px;display:flex;align-items:center}
.hero{left:210px;top:194px;width:1000px;height:431px;border:3px solid #e6e6e6;background:#fff}
.hero-photo{position:absolute;left:0;top:0;width:617px;height:425px;
  background:linear-gradient(90deg,#f4f4f4,#d9dde6 30%,#c9d3e6 60%,#f1f1f1)}
.hero-title{position:absolute;left:607px;top:120px;font:500 40px/1 Cabin,sans-serif;color:var(--ink)}
.hero-sub{position:absolute;left:609px;top:172px;font:26px/35px "Crimson Text",Georgia,serif;color:var(--accent-blue)}
.dots{position:absolute;left:880px;top:395px;display:flex;gap:5px}
.dots i{width:13px;height:13px;border-radius:50%;background:#222;border:1px solid #555}
.dots i.on{background:var(--navy)}
.panel{left:210px;width:282px;color:#fff;padding:0 13px 0 26px}
.panel h2{font:400 18px/1 Cabin,sans-serif;padding:21px 0 10px;border-bottom:1px solid rgba(255,255,255,.25)}
.services{top:635px;height:306px;background:var(--services-bg)}
.services ul{list-style:none;margin-top:10px}
.services li{font-size:12px;height:32px;line-height:20px;padding-left:20px;position:relative}
.services li::before{content:"»";position:absolute;left:3px;top:-1px;color:var(--bullet);font-size:11px}
.btn{display:inline-block;height:32px;padding:0 13px;line-height:31px;font-size:12px;color:#222;
  background:linear-gradient(#f6f7f9,#cfd4da);border:1px solid #b9bec5}
.services .btn{position:absolute;left:36px;top:259px}
.testimonials{top:951px;height:256px;background:var(--testimonial-bg)}
.testimonials .who{font:700 12px/1 Arimo,sans-serif;margin:20px 0 0 5px}
.testimonials p{font-size:12px;line-height:18px;margin:20px 0 0 5px}
.testimonials .btn{position:absolute;left:36px;top:208px}
.section-title{font:400 18px/1 Cabin,sans-serif;color:#222}
.lead{font-weight:700;font-size:12px;line-height:18px;color:#000}
.copy{font-size:12px;line-height:18px;color:var(--body-text)}
.photo{background:linear-gradient(135deg,#c9cbd0,#8e96a3);border:1px solid #999}
.social{left:1058px;top:1256px;display:flex;gap:10px}
.social i{width:22px;height:22px;border-radius:3px}
.footer-links{left:216px;top:1248px;font-size:12px;color:var(--muted)}
.footer-links span{margin-right:13px}
.footer-copy{left:216px;top:1272px;font-size:12px;color:var(--muted)}
</style>
</head>
<body>
<div class="page">
  <div class="abs brand">
    <span class="brand-mark"></span>
    <div>
      <div class="brand-name">FiberTend Pro</div>
      <div class="brand-sub">HARBORLINE CLEANING, LLC</div>
    </div>
  </div>
  <div class="abs search">Search
    <svg width="12" height="12" viewBox="0 0 12 12"><circle cx="4.5" cy="4.5" r="3.3" fill="none" stroke="#333" stroke-width="1.6"/><line x1="7" y1="7" x2="11" y2="11" stroke="#333" stroke-width="2"/></svg>
  </div>

  <nav class="abs nav">
    <a href="#">HOME</a><a href="#">ABOUT</a><a href="#">SERVICES</a><a href="#">SPECIAL OFFERS</a><a href="#">TESTIMONIALS</a><a href="#">CONTACTS</a>
  </nav>

  <section class="abs hero">
    <div class="hero-photo" role="img" aria-label="Two smiling cleaners in aprons holding cleaning tools and a bucket of supplies"></div>
    <div class="hero-title">PROFESSIONAL</div>
    <div class="hero-sub">residential and commercial<br>carpet cleaning services</div>
    <div class="dots"><i></i><i class="on"></i><i></i><i></i></div>
  </section>

  <aside class="abs panel services">
    <h2>OUR SERVICES</h2>
    <ul>
      <li>Fine Rug Cleaning</li><li>Upholstery Cleaning</li><li>Carpet Cleaning</li>
      <li>Water Damage Restoration</li><li>Pet Odor Treatment</li><li>Stain &amp; Moth Protection</li>
    </ul>
    <a class="btn">Read More</a>
  </aside>

  <aside class="abs panel testimonials">
    <h2>TESTIMONIALS</h2>
    <div class="who">mr. Evan Pollard</div>
    <p>Soluta nobis est eligendi omnis voluas assumenda est, omnis doloresed rees eldusempquibusdamet aut officiis aste necessitatibus saepe eveniet ut etred voluptates repudiandae sit</p>
    <a class="btn">Read More</a>
  </aside>

  <h2 class="abs section-title" style="left:508px;top:648px">WELCOME TO OUR FIBERTEND PRO SITE</h2>
  <div class="abs photo" style="left:508px;top:684px;width:229px;height:201px" role="img" aria-label="Worker mopping the floor of a glass-walled hall"></div>
  <p class="abs lead" style="left:749px;top:685px;width:450px">At vero eos et accusamus et iusto odio dignissimoupiditate non prodent simi-lique officia deserunt mollitiase animi, id est laborum et dolorum</p>
  <p class="abs copy" style="left:749px;top:739px;width:460px">At vero eos et accusamus et iusto odio dignissimos ducimuse dolore massa astu edAt vero eetre accusamus corrupti quos dolores et quas molestias exceturinocca- ecati cupiditate non providenas similique sunt in culpa officia deserunt mollitia imiid est laborum et dolorum fuga. Et harund quidem rerum facilis est et expedita</p>
  <a class="abs btn" style="left:749px;top:829px">Read More</a>

  <h2 class="abs section-title" style="left:508px;top:949px">CLEANING ADVICE</h2>
  <p class="abs lead" style="left:508px;top:986px;width:380px">Massa ipsum dolode sed laoreet&nbsp; sit ametonume onsectetur adipi-sicing elit, sedomo eiusmod tempor</p>
  <p class="abs copy" style="left:508px;top:1040px;width:382px">Massa ipsum dolode sed laoreet&nbsp; sit ametonume onsectetur adipisicing elit, sedomo eiusmod tempor et dolore magna aliqua. Utel enaded minim veniam, quis nostrud xercitation ullamco laborinisut ex ea com-modo consequat mass. Duis aute irure dolor in reprehenderit in volup-tate velit esse cillum dolore eu fugiat</p>
  <a class="abs btn" style="left:509px;top:1159px">Read More</a>

  <h2 class="abs section-title" style="left:919px;top:949px">OUR GALLERY</h2>
  <div class="abs photo" style="left:920px;top:987px;width:134px;height:103px;background:linear-gradient(#aac4e0,#d8d8d8)" role="img" aria-label="Window washers working on a glass facade"></div>
  <div class="abs photo" style="left:1068px;top:987px;width:134px;height:103px;background:linear-gradient(135deg,#5f7fa8,#c9733a)" role="img" aria-label="Worker in safety vest and helmet cleaning windows"></div>
  <div class="abs photo" style="left:920px;top:1104px;width:134px;height:103px;background:linear-gradient(135deg,#6f9aaa,#8a7f62)" role="img" aria-label="Worker in helmet wiping a window with a squeegee"></div>
  <div class="abs photo" style="left:1068px;top:1104px;width:134px;height:103px;background:linear-gradient(135deg,#c4c8cc,#d9b64a)" role="img" aria-label="Gloved hand cleaning window blinds with a sponge"></div>

  <div class="abs" style="left:210px;top:1233px;width:1000px;height:1px;background:var(--rule)"></div>
  <div class="abs footer-links"><span>HOME</span><span>ABOUT US</span><span>SERVICES</span><span>SUPPORT</span><span>TIPS</span><span>LOCATIONS</span><span>CONTACTS</span></div>
  <div class="abs footer-copy">FiberTend Pro © 2012 | Copyright | All Rights Reseverd |&nbsp; Privacy Policy</div>
  <div class="abs" style="left:917px;top:1262px;font-size:12px;color:var(--muted)">M3</div>
  <div class="abs social">
    <i style="background:#3b5998"></i><i style="background:#4fb3e0"></i><i style="background:#1d76b3"></i><i style="background:#f28a1c"></i><i style="background:#c4302b"></i>
  </div>
</div>
</body>
</html>
```